Website Layout for Upcoming Crowdfunding ICO - Digital Currency

We need our website redesigned in a responsive format. Must be attractive with countdown timer to launch, video embedded, PDF whitepaper link, roadmap, team section and contact form. Current website on www.quillomark.io Experience in previous ICO website designs a plus

Websites that stand out
https://veltrisoken.com/
https://greyharborvault.com/
http://ico.silvanomet.com/
https://www.zumbrelle.io/

Target Market(s)

Tavrimo Investors
Traders
Forex traders
Solvanex Traders
ICO investors

Industry/Entity Type

Digital

Coding

Coded - Design and coding required

Number of Pages Required

1 page

Font styles to use
Sans Serif

Colors

Designer to choose colors to be used in the design.

Requirements
Must have
• countdown timer to launch, video embedded, PDF whitepaper link, roadmap, team section and contact form sections
Should not have
• Soft colors

```html
<!DOCTYPE html>
<html lang="en">
<head>
<meta charset="utf-8">
<title>Quillomark ICO</title>
<link href="https://fonts.googleapis.com/css2?family=Lato:wght@400;700;900&display=swap" rel="stylesheet">
<style>
:root{
  --navy:#17344f;
  --blue:#1f6aa5;
  --blue-deep:#14507f;
  --blue-light:#2c86c7;
  --ink:#222831;
  --text:#4a4f55;
  --muted:#8a9098;
  --grey-bg:#eceef0;
  --line:#d6dade;
  --white:#ffffff;
  --dark:#1d1f22;
  --footer-grey:#5d6166;
}
*{box-sizing:border-box;margin:0;padding:0}
html,body{width:1200px;height:5000px;overflow:hidden}
body{font-family:'Lato',sans-serif;color:var(--text);background:var(--white);position:relative}
section,header,footer{position:absolute;left:0;width:1200px}
h2{font-weight:900;color:var(--ink);font-size:34px;letter-spacing:.5px}
.sub{font-size:14px;color:var(--muted)}
.btn{display:inline-block;background:var(--dark);color:var(--white);font-weight:700;font-size:13px;letter-spacing:1px;border-radius:22px;padding:11px 26px}

/* hero */
.hero{top:0;height:485px;background:linear-gradient(180deg,#0e1114,#20262c)}
.nav{position:absolute;top:0;left:0;width:1200px;height:62px;display:flex;align-items:center;padding:0 60px}
.brand{font-size:30px;font-weight:700;color:var(--white)}
.menu{margin-left:auto;display:flex;gap:28px;font-size:13px;font-weight:700;color:var(--white);letter-spacing:.5px}
.lang{margin-left:26px;background:var(--white);color:var(--ink);font-size:12px;padding:4px 12px;border-radius:2px}
.hero-art{position:absolute;left:60px;top:62px;width:1080px;height:423px;background:radial-gradient(ellipse at 50% 55%,#3f5f73 0%,#1f3442 45%,#12181d 80%)}
.coin-art{position:absolute;left:420px;top:90px;width:360px;height:360px;border-radius:50%;background:radial-gradient(circle at 40% 35%,#f4d27a,#c8902a 70%,#8a5d14)}

/* countdown */
.countdown{top:485px;height:290px;text-align:center;padding-top:52px}
.countdown h2{font-size:36px}
.countdown .sub{margin-top:12px;font-size:13px;letter-spacing:1px}
.timer{display:flex;justify-content:center;align-items:center;margin-top:30px;gap:8px}
.digit{width:50px;height:62px;background:var(--blue-deep);color:var(--white);font-size:38px;font-weight:700;display:flex;align-items:center;justify-content:center;border-radius:6px}
.colon{font-size:36px;font-weight:700;color:var(--navy);margin:0 10px}
.units{display:flex;justify-content:center;gap:0;margin-top:14px;font-size:15px;color:var(--text)}
.units span{width:182px}

/* business model */
.model{top:775px;height:705px;background:linear-gradient(135deg,#1b5f96,#2a80bf)}
.phone-art{position:absolute;left:0;top:0;width:520px;height:705px;background:linear-gradient(160deg,#5fa3d6,#2a6ea6 60%,#1b5a8c)}
.model-copy{position:absolute;left:550px;top:45px;width:600px;color:var(--white)}
.model-copy h2{color:var(--white);font-size:34px}
.model-copy .lead{font-size:16px;margin-top:10px;line-height:1.45;font-weight:700}
.features{display:grid;grid-template-columns:repeat(3,1fr);gap:40px 30px;margin-top:38px}
.feature .ico{width:46px;height:46px;border:2px solid var(--white);border-radius:8px;display:flex;align-items:center;justify-content:center}
.feature h3{font-size:19px;font-weight:700;margin-top:14px;line-height:1.25}
.feature p{font-size:13px;line-height:1.55;margin-top:8px;opacity:.9}

/* why invest */
.why{top:1480px;height:420px}
.why-left{position:absolute;left:60px;top:40px;width:520px}
.why-left h2{font-size:30px}
.point{margin-top:26px}
.point h4{font-size:15px;font-weight:900;color:var(--blue);display:flex;align-items:center;gap:10px}
.point h4 i{width:16px;height:16px;border-radius:50%;background:var(--blue);display:inline-block}
.point p{font-size:13px;line-height:1.6;margin-top:10px}
.why-right{position:absolute;left:640px;top:40px;width:500px}
.why-right h2{font-size:30px;text-align:center}
.video{margin-top:22px;height:290px;background:linear-gradient(135deg,#e9eef3,#b9cde0 60%,#2a7fc0);position:relative}
.video-bar{position:absolute;left:0;top:0;width:100%;height:28px;background:rgba(20,30,40,.75);color:var(--white);font-size:12px;padding:7px 12px}
.play{position:absolute;left:220px;top:115px;width:60px;height:60px;border-radius:50%;background:rgba(0,0,0,.6);display:flex;align-items:center;justify-content:center}

/* participate */
.participate{top:1900px;height:485px;background:var(--grey-bg);text-align:center;padding-top:40px}
.participate h2{font-size:34px}
.participate .gap{margin-top:26px}
.steps{position:relative;display:flex;justify-content:space-between;width:960px;margin:48px auto 0}
.steps-line{position:absolute;left:160px;right:160px;top:36px;height:3px;background:var(--blue)}
.step{width:300px;position:relative}
.step .circle{width:74px;height:74px;border-radius:50%;background:var(--blue);margin:0 auto;display:flex;align-items:center;justify-content:center}
.step h3{font-size:20px;color:var(--ink);margin-top:20px;font-weight:700}
.step p{font-size:13px;line-height:1.6;margin-top:14px}

/* whitepaper */
.whitepaper{top:2385px;height:200px;background:linear-gradient(90deg,#0d2b46,#15508a 55%,#0d2b46)}
.wp-art{position:absolute;left:0;top:0;width:500px;height:200px;background:linear-gradient(90deg,#1f8aa0,#15508a)}
.wp-copy{position:absolute;left:610px;top:62px;color:var(--white)}
.wp-copy h2{color:var(--white);font-size:32px}
.wp-copy p{font-size:15px;margin-top:6px}
.wp-btn{position:absolute;left:910px;top:76px;background:var(--white);color:var(--ink);font-weight:900;font-size:14px;padding:14px 26px;border-radius:4px;display:flex;gap:10px;align-items:center}

/* roadmap */
.roadmap{top:2585px;height:615px;text-align:center;padding-top:32px}
.roadmap h2{font-size:32px}
.roadmap .sub{margin-top:6px}
.rm-svg{position:absolute;left:0;top:0}
.milestone{position:absolute;text-align:left;width:210px}
.milestone .date{font-size:14px;font-weight:900;color:var(--ink)}
.milestone h4{font-size:15px;font-weight:700;color:var(--ink);margin-top:2px}
.milestone p{font-size:12px;line-height:1.55;margin-top:8px}
.rm-photo{position:absolute;border-radius:50%;background:linear-gradient(135deg,#4a4f55,#1d1f22)}
.rm-story{position:absolute;left:900px;top:265px;width:120px;height:120px;border-radius:50%;background:var(--dark);color:var(--white);font-weight:900;font-size:15px;display:flex;align-items:center;justify-content:center;text-align:center;line-height:1.3}

/* join */
.join{top:3200px;height:270px;background:linear-gradient(135deg,#1b5f96,#2c86c7);text-align:center;padding-top:48px;color:var(--white)}
.join h2{color:var(--white);font-size:34px}
.join p{font-size:14px;margin-top:10px;line-height:1.5}
.join-form{display:flex;justify-content:center;gap:10px;margin-top:28px}
.join-form .field{width:440px;height:42px;border-radius:22px;background:var(--white);color:var(--muted);font-size:13px;text-align:left;padding:12px 22px}

/* team */
.team{top:3470px;height:500px;text-align:center;padding-top:40px}
.team h2{font-size:32px}
.cards{display:flex;justify-content:center;gap:40px;margin-top:36px}
.card{width:300px;height:330px;box-shadow:0 2px 14px rgba(0,0,0,.12);padding-top:40px}
.portrait{width:160px;height:160px;border-radius:50%;margin:0 auto;background:linear-gradient(160deg,#c9ccd0,#5e636a)}
.card h3{font-size:20px;color:var(--ink);margin-top:22px;font-weight:700}
.card .role{font-size:12px;margin-top:4px}
.card .btn{margin-top:14px;padding:7px 20px;font-size:11px}
.arrow{position:absolute;top:235px}

/* faq */
.faq{top:3970px;height:460px;padding:40px 0 0 100px}
.faq h2{font-size:32px}
.faq-list{width:1000px;margin-top:28px}
.faq-item{border:1px solid var(--line);padding:16px 24px;font-size:15px;color:var(--ink);display:flex;align-items:center;gap:14px;margin-top:-1px}
.faq-item.open{background:#f6f7f8}
.faq-answer{border:1px solid var(--line);border-top:0;padding:18px 24px;font-size:13px;line-height:1.55;display:flex;gap:14px;margin-top:-1px}
.faq-answer i{width:10px;height:10px;border-radius:50%;background:var(--blue);flex:none;margin-top:4px}

/* footer */
.site-footer{top:4430px;height:570px}
.foot-about{position:absolute;left:0;top:0;width:455px;height:500px;background:var(--footer-grey);color:#e8e9ea;padding:40px 60px 0 100px}
.foot-about .brand{font-size:30px}
.foot-about p{font-size:13px;line-height:1.7;margin-top:22px}
.foot-links{position:absolute;left:455px;top:0;width:225px;height:500px;background:#2a2d31;color:var(--white);padding:40px 30px}
.foot-links h4,.foot-contact h4{font-size:18px;font-weight:900}
.foot-links ul{list-style:none;margin-top:24px}
.foot-links li{font-size:12px;margin-bottom:14px;display:flex;gap:10px;align-items:center}
.foot-links li::before{content:"";width:5px;height:5px;background:var(--white);border-radius:50%}
.foot-contact{position:absolute;left:680px;top:0;width:520px;height:500px;background:var(--blue);color:var(--white);padding:40px 60px 0 40px}
.foot-contact .sub{color:#d7e6f3;margin-top:8px;font-size:12px}
.input{background:var(--white);color:var(--muted);font-size:12px;padding:11px 14px;margin-top:12px;height:38px}
.input.tall{height:80px}
.send{margin:18px auto 0;width:200px;background:var(--blue-deep);text-align:center;font-weight:700;font-size:13px;padding:11px 0;letter-spacing:.5px}
.bottom-bar{position:absolute;left:0;top:500px;width:1200px;height:70px;background:var(--dark);color:#b8bcc0;font-size:12px;display:flex;align-items:center;padding:0 100px}
.socials{margin-left:auto;display:flex;gap:10px}
.socials span{width:28px;height:28px;border-radius:50%;background:var(--blue-light)}
</style>
</head>
<body>

<header class="hero">
  <div class="hero-art" role="img" aria-label="Dark world map of dots behind a large gold coin">
    <div class="coin-art"></div>
  </div>
  <nav class="nav">
    <div class="brand">quillomark</div>
    <div class="menu"><span>VIDEO</span><span>CROWDSALE</span><span>JOIN OUR ICO</span><span>WHITE PAPER</span><span>ABOUT TEAM</span><span>FAQ</span><span>CONTACT</span></div>
    <div class="lang">English</div>
  </nav>
</header>

<section class="countdown">
  <h2>COUNTDOWN TO CROWDSALE</h2>
  <p class="sub">CROWDSALE STARTS 20 NOVEMBER 2017</p>
  <div class="timer">
    <div class="digit">3</div><div class="digit">7</div><span class="colon">:</span>
    <div class="digit">2</div><div class="digit">0</div><span class="colon">:</span>
    <div class="digit">0</div><div class="digit">7</div><span class="colon">:</span>
    <div class="digit">2</div><div class="digit">0</div>
  </div>
  <div class="units"><span>Days</span><span>Hours</span><span>Minutes</span><span>Seconds</span></div>
</section>

<section class="model">
  <div class="phone-art" role="img" aria-label="Hand holding a smartphone surrounded by currency symbols"></div>
  <div class="model-copy">
    <h2>OUR BUSINESS MODEL</h2>
    <p class="lead">Our Clear Cut Business Model On How We Re Providing Value For Investors And Plans To Continue Add Value To The Token Long After The Crowdsale Closes</p>
    <div class="features">
      <div class="feature">
        <div class="ico"><svg width="24" height="24" viewBox="0 0 24 24" fill="none" stroke="#fff" stroke-width="2"><rect x="2" y="6" width="20" height="12"/><circle cx="12" cy="12" r="3"/></svg></div>
        <h3>Raise Funds</h3>
        <p>Our crowdsale will aim to raise $20 Million over a period of 4 weeks and 1 day.</p>
      </div>
      <div class="feature">
        <div class="ico"><svg width="24" height="24" viewBox="0 0 24 24" fill="none" stroke="#fff" stroke-width="2"><circle cx="8" cy="8" r="3"/><circle cx="16" cy="8" r="3"/><path d="M2 20c0-4 3-6 6-6s6 2 6 6M12 20c0-4 2-6 4-6s6 2 6 6"/></svg></div>
        <h3>Setup our Team</h3>
        <p>Using the funds raised and the percentages allocated we setup our team to get the ball rolling.</p>
      </div>
      <div class="feature">
        <div class="ico"><svg width="24" height="24" viewBox="0 0 24 24" fill="none" stroke="#fff" stroke-width="2"><path d="M3 11l9-7 9 7v10H3z"/><rect x="9" y="14" width="6" height="7"/></svg></div>
        <h3>Buy Property</h3>
        <p>Our team will search for good property investments and carry out due diligence before making the purchase.</p>
      </div>
      <div class="feature">
        <div class="ico"><svg width="24" height="24" viewBox="0 0 24 24" fill="none" stroke="#fff" stroke-width="2"><rect x="3" y="4" width="18" height="12"/><path d="M8 20h8M12 16v4"/></svg></div>
        <h3>Develop Investor Platform</h3>
        <p>Token holders can use our investor platform to track their tokens and new properties linked to our portfolio.</p>
      </div>
      <div class="feature">
        <div class="ico"><svg width="24" height="24" viewBox="0 0 24 24" fill="none" stroke="#fff" stroke-width="2"><path d="M4 20V10M10 20V4M16 20v-8M22 20H2"/></svg></div>
        <h3>Funds Administration System</h3>
        <p>Profit earned are paid in Solvanex (SVX) or any future equivalent cryptocurrency to the digital wallet address used by the investor.</p>
      </div>
      <div class="feature">
        <div class="ico"><svg width="24" height="24" viewBox="0 0 24 24" fill="none" stroke="#fff" stroke-width="2"><path d="M3 17l6-6 4 4 8-8M15 7h6v6"/></svg></div>
        <h3>Trading on the Exchanges</h3>
        <p>Our tokens will be listed on the major cryptocurrency exchanges with high trading volumes.</p>
      </div>
    </div>
  </div>
</section>

<section class="why">
  <div class="why-left">
    <h2>WHY INVEST IN OUR ICO?</h2>
    <div class="point">
      <h4><i></i>TANGIBLE ASSET BACKING THE COIN</h4>
      <p>Property provides good annual returns of between 8 - 10% depending on jurisdiction. Property is relatively stable unlike the stock market with the risks of major fluctuations in value. The capital investment appreciates over the long run and does so consistently.</p>
    </div>
    <div class="point">
      <h4><i></i>COIN VALUE IS IMPORTANT TO US</h4>
      <p>The general trend with ICO and currency coins is that the cheaper they are the more volatile they are. We have engineered a way for the coin to only be sold in a bullish market where investors can buy with profit and benefit from the company behind the coin.</p>
    </div>
  </div>
  <div class="why-right">
    <h2>QUILLOMARK EXPLAINED</h2>
    <div class="video" role="img" aria-label="Embedded explainer video still showing a presenter beside a rising bar chart">
      <div class="video-bar">Quillomark</div>
      <div class="play"><svg width="22" height="22" viewBox="0 0 22 22"><path d="M6 3l13 8-13 8z" fill="#fff"/></svg></div>
    </div>
  </div>
</section>

<section class="participate">
  <h2>CONTRACT ADDRESS</h2>
  <p class="sub">Contract Address Will Be Published 48hrs Before Launch</p>
  <h2 class="gap">HOW DO I PARTICIPATE?</h2>
  <p class="sub">How To Invest In The Quillomark Initial Coin Offering (Ico)</p>
  <div class="steps">
    <div class="steps-line"></div>
    <div class="step">
      <div class="circle"><svg width="30" height="30" viewBox="0 0 24 24" fill="none" stroke="#fff" stroke-width="2"><path d="M12 3v18M3 12h18"/></svg></div>
      <h3>Buy Solvex</h3>
      <p>Signup for a Cryptocurrency Wallet account and download the app if you're using a mobile phone. Buy Solvex in your currency from the wallet website or app.</p>
    </div>
    <div class="step">
      <div class="circle"><svg width="30" height="30" viewBox="0 0 24 24" fill="none" stroke="#fff" stroke-width="2"><path d="M4 8h15l-4-4M20 16H5l4 4"/></svg></div>
      <h3>Transfer Solvex</h3>
      <p>Once you have successfully purchased your Solvanex currency you can send the amount of Solvex you wish to invest to the Crowdsale contract address above.</p>
    </div>
    <div class="step">
      <div class="circle"><svg width="30" height="30" viewBox="0 0 24 24" fill="none" stroke="#fff" stroke-width="2"><path d="M12 3v13M6 10l6 6 6-6M4 21h16"/></svg></div>
      <h3>Receive Tokens</h3>
      <p>For every 1 Solvex we issue an amount of Quillomark Tokens or Coins based on the times remaining for investment. Early investors get the most value per Solvex sent to our token contract.</p>
    </div>
  </div>
</section>

<section class="whitepaper">
  <div class="wp-art" role="img" aria-label="Blue network and circuit background imagery"></div>
  <div class="wp-copy">
    <h2>WHITEPAPER</h2>
    <p>Download Our Whitepaper</p>
  </div>
  <div class="wp-btn"><svg width="16" height="16" viewBox="0 0 24 24" fill="none" stroke="#222831" stroke-width="3"><path d="M12 3v13M6 10l6 6 6-6M4 21h16"/></svg>DOWNLOAD NOW</div>
</section>

<section class="roadmap">
  <h2>ROADMAP</h2>
  <p class="sub">Timeline Of Events Leading Up To Our Ico</p>
  <svg class="rm-svg" width="1200" height="615" viewBox="0 0 1200 615" fill="none">
    <path d="M60 330 C 120 300, 200 330, 240 345 S 320 390, 352 378 S 470 400, 560 385 S 680 300, 760 300 S 860 330, 900 325" stroke="#4a4f55" stroke-width="2"/>
  </svg>
  <div class="rm-photo" style="left:95px;top:265px;width:140px;height:140px" role="img" aria-label="Business plan document photo"></div>
  <div class="rm-photo" style="left:295px;top:320px;width:115px;height:115px" role="img" aria-label="ICO concept keyboard photo"></div>
  <div class="milestone" style="left:95px;top:430px">
    <div class="date">JUNE 2017</div><h4>Our Beginnings</h4>
    <p>Founders create Quillomark's sale funds to purchase properties throughout the world and create a portfolio to back the Quillomark Token.</p>
  </div>
  <div class="milestone" style="left:300px;top:175px">
    <div class="date">JULY 2017</div><h4>An ICO is Born</h4>
    <p>The founders choose the Solvanex blockchain platform as a base to build the Quillomark Token.</p>
  </div>
  <div class="milestone" style="left:500px;top:420px">
    <div class="date">NOVEMBER 2017</div><h4>Gather Investors</h4>
    <p>Through our detailed and transparent whitepaper which outlines our goals for setting up the Quillomark business we rally investors.</p>
  </div>
  <div class="milestone" style="left:700px;top:125px;width:230px">
    <div class="date">JANUARY 2018</div><h4>Transition to Full Service</h4>
    <p>Once the crowdsale period has finished, the founders list the token on the Cryptocurrency Exchanges and carry out the business plan as detailed in the Whitepaper.</p>
  </div>
  <div class="rm-story">BE PART<br>OF OUR<br>STORY</div>
</section>

<section class="join">
  <h2>JOIN OUR ICO</h2>
  <p>Lorem ipsum dolor sit amet, consectetur adipiscing elit. Ut<br>congue erat at ante rutrum dapibus. Pellentesque suscipit quam</p>
  <div class="join-form">
    <div class="field">Email</div>
    <div class="btn">JOIN NOW</div>
  </div>
</section>

<section class="team">
  <h2>OUR TEAM</h2>
  <svg class="arrow" style="left:30px" width="20" height="30" viewBox="0 0 20 30"><path d="M15 3L4 15l11 12" stroke="#4a4f55" stroke-width="2" fill="none"/></svg>
  <svg class="arrow" style="left:1150px" width="20" height="30" viewBox="0 0 20 30"><path d="M5 3l11 12L5 27" stroke="#4a4f55" stroke-width="2" fill="none"/></svg>
  <div class="cards">
    <div class="card"><div class="portrait" role="img" aria-label="Portrait photo of the CEO"></div><h3>DORIAN VELL</h3><p class="role">CEO, Founder</p><span class="btn">READ BIO</span></div>
    <div class="card"><div class="portrait" role="img" aria-label="Portrait photo of the CMO"></div><h3>HOLT MARAVEN</h3><p class="role">CMO, Co-Founder</p><span class="btn">READ BIO</span></div>
    <div class="card"><div class="portrait" role="img" aria-label="Portrait photo of the CTO"></div><h3>ANSEL KIRROW</h3><p class="role">CTO, Co-Founder</p><span class="btn">READ BIO</span></div>
  </div>
</section>

<section class="faq">
  <h2>FAQ</h2>
  <div class="faq-list">
    <div class="faq-item open"><svg width="10" height="10" viewBox="0 0 10 10"><path d="M1 3l4 4 4-4" stroke="#222831" stroke-width="1.5" fill="none"/></svg>When does the crowdsale start?</div>
    <div class="faq-answer"><i></i>Our crowdsale starts officially on the 20 November 2017 with the first day being our stage day for investors to get the most tokens per 1 Solvex.</div>
    <div class="faq-item"><svg width="10" height="10" viewBox="0 0 10 10"><path d="M3 1l4 4-4 4" stroke="#222831" stroke-width="1.5" fill="none"/></svg>What does your token give me?</div>
    <div class="faq-item"><svg width="10" height="10" viewBox="0 0 10 10"><path d="M3 1l4 4-4 4" stroke="#222831" stroke-width="1.5" fill="none"/></svg>Do you have a capped crowdsale?</div>
    <div class="faq-item"><svg width="10" height="10" viewBox="0 0 10 10"><path d="M3 1l4 4-4 4" stroke="#222831" stroke-width="1.5" fill="none"/></svg>What currencies do you accept?</div>
  </div>
</section>

<footer class="site-footer">
  <div class="foot-about">
    <div class="brand">quillomark</div>
    <p>Suspendisse risus urna, dapibus et erat id, scelerisque bibendum dui. Ut non nisl ac justo tempor cursus sed sit amet. Pellentesque pharetra ac justo ut imperdiet. Curabitur non suscipit diam. Quisque in laoreet ipsum, vel dapibus est. Nulla pellentesque faucibus vulputate.</p>
  </div>
  <div class="foot-links">
    <h4>QUICK LINKS</h4>
    <ul><li>VIDEO</li><li>CROWDSALE</li><li>JOIN OUR ICO</li><li>WHITEPAPER</li><li>ABOUT</li><li>TEAM</li><li>FAQ</li><li>CONTACT</li></ul>
  </div>
  <div class="foot-contact">
    <h4>CONTACT US</h4>
    <p class="sub">ANY QUESTIONS ABOUT INVESTING, SEND THEM OUR WAY</p>
    <div class="input">Name</div>
    <div class="input">Email Address</div>
    <div class="input">Phone</div>
    <div class="input tall">Your Message Here</div>
    <div class="send">SEND MESSAGE</div>
  </div>
  <div class="bottom-bar">
    <span>Copyright © 2017 Quillomark. All rights reserved.</span>
    <div class="socials"><span></span><span></span></div>
  </div>
</footer>

</body>
</html>
```